Interfaith organization needs a poster advertising event for youth

We need a poster advertising our annual Lantern Gathering and Summit, where youth of all different religions come together for dialogue, friendship, fun, art, and musical performances. The poster should be have a front advertising the event, and the back should have more detailed descriptions of the event and submissions. It should be fun and eye catching!

Target Market(s)

Youth and Religious Organizations

Industry/Entity Type

Festival

Font styles to use
Serif

Requirements
Must have
• Pictures, poster-feel, contact information, etc. Logos of Bright Harbor Allies and Crossroads Young Leaders Circle of Maple Valley

```html
<!DOCTYPE html>
<html lang="en">
<head>
<meta charset="utf-8">
<title>Lantern Gathering and Summit Poster</title>
<link href="https://fonts.googleapis.com/css2?family=Kaushan+Script&family=Roboto+Condensed:wght@400;700&display=swap" rel="stylesheet">
<style>
:root{
  --stage:#1d1b18;
  --brown-dark:#2e1a0a;
  --brown:#6b4212;
  --gold:#b8901e;
  --yellow-band:#c9b22a;
  --title-orange:#d98a2a;
  --headline-yellow:#f2e022;
  --ink:#111;
  --white:#fff;
  --red:#c2341f;
  --partner-blue:#2d5fa8;
  --seal-gold:#a88a4a;
}
*{box-sizing:border-box;margin:0;padding:0}
html,body{width:1200px;height:1200px;overflow:hidden;background:var(--stage)}
body{position:relative;font-family:"Roboto Condensed",sans-serif;color:var(--white)}
.flyer{position:absolute;width:537px;height:818px;overflow:hidden;
  background:radial-gradient(ellipse at 50% 55%,#8d6a1a 0%,var(--brown) 45%,var(--brown-dark) 100%)}
.flyer--front{left:30px;top:194px}
.flyer--back{left:613px;top:196px}
.council-title{position:absolute;top:16px;left:0;width:100%;text-align:center;font-weight:400;
  font-family:"Kaushan Script",cursive;color:var(--title-orange);font-size:31px;line-height:40px}
.partner-box{position:absolute;top:106px;width:148px;height:92px;background:var(--white);
  display:flex;align-items:center;justify-content:center;text-align:center;gap:6px;padding:8px}
.partner-box--left{left:0;border-radius:0 10px 10px 0}
.partner-box--right{right:0;border-radius:10px 0 0 10px}
.partner-name{font-size:17px;font-weight:700;line-height:1.1;color:var(--partner-blue)}
.partner-box--right .partner-name{color:var(--seal-gold);font-size:12px}
.partner-dot{flex:none;width:26px;height:26px;border-radius:50%;border:2px solid var(--seal-gold)}
.edition{position:absolute;top:110px;left:148px;width:241px;text-align:center;font-family:"Kaushan Script",cursive}
.edition-year{font-size:34px;color:var(--white);line-height:42px}
.edition-name{font-size:27px;color:var(--headline-yellow);line-height:33px}
.tagline{position:absolute;left:0;width:100%;text-align:center;text-transform:uppercase;font-size:19px;line-height:27px}
.flyer--front .tagline{top:232px;padding:0 50px}
.flyer--back .tagline{top:232px;font-size:16px}
.theme-panel{position:absolute;left:0;top:287px;width:213px;height:213px;background:var(--yellow-band);
  color:var(--ink);text-align:center;padding-top:12px}
.theme-panel .big{font-size:32px;font-weight:700;line-height:34px}
.theme-panel .mid{font-size:25px;line-height:28px}
.theme-panel .theme{font-size:30px;font-weight:700;margin-top:12px}
.photo{position:absolute}
.p1{left:215px;top:287px;width:106px;height:105px;background:linear-gradient(#8a7a6a,#4a3a30)}
.p2{left:324px;top:287px;width:106px;height:105px;background:linear-gradient(#6a8080,#3a4448)}
.p3{left:432px;top:287px;width:105px;height:105px;background:linear-gradient(#d9b59a,#8a6a5a)}
.p4{left:215px;top:394px;width:106px;height:104px;background:linear-gradient(#b09a8a,#5a4038)}
.p5{left:324px;top:394px;width:213px;height:212px;background:linear-gradient(135deg,#7a5a48,#3a2520)}
.p6{left:0;top:501px;width:106px;height:212px;background:linear-gradient(#a89888,#5a3a28)}
.p7{left:108px;top:501px;width:105px;height:105px;background:linear-gradient(#c8c0c8,#7a6a70)}
.p8{left:215px;top:501px;width:106px;height:105px;background:linear-gradient(#8a8aa0,#4a4a5a)}
.p9{left:108px;top:608px;width:322px;height:210px;background:linear-gradient(135deg,#d8d0c8,#8a2a28)}
.p10{left:432px;top:608px;width:105px;height:210px;background:linear-gradient(#c8a0a0,#a8302a)}
.p11{left:0;top:715px;width:106px;height:103px;background:linear-gradient(#e8e8ee,#2a2a2a)}
.forum-head{position:absolute;left:0;width:100%;text-align:center;text-transform:uppercase}
.forum-head--label{top:262px;font-size:23px;line-height:28px;font-weight:700}
.forum-head--intro{top:292px;font-size:20px;line-height:24px}
.forum-head--theme{top:316px;font-size:48px;line-height:46px;font-weight:700;letter-spacing:.5px}
.info-band{position:absolute;left:0;top:366px;width:100%;height:168px;background:var(--yellow-band);color:var(--ink)}
.when{display:flex;justify-content:center;margin-top:6px}
.when div{width:175px;text-align:center;font-weight:700;font-size:17px;line-height:23px}
.when div:first-child{border-right:1px solid rgba(0,0,0,.4)}
.venue{margin:6px auto 0;width:278px;background:var(--red);color:var(--white);border-radius:10px;
  text-align:center;font-size:13px;line-height:18px;padding:2px 0}
.venue strong{display:block;font-size:14px}
.invite{font-size:10px;line-height:13px;text-align:center;padding:8px 26px 0}
.detail-col{position:absolute;text-align:center}
.detail-col h3{color:var(--headline-yellow);font-size:16px;margin-bottom:6px;white-space:nowrap}
.detail-col p{font-size:7.4px;line-height:9.8px;text-align:justify;color:#f3ead8}
.detail-col .cta{font-size:18px;font-weight:700;color:var(--white);line-height:22px;margin-top:6px;white-space:nowrap}
.detail-col .rsvp{font-size:12px;line-height:17px;font-weight:700}
.detail-col .rsvp em{display:block;font-style:normal;color:var(--headline-yellow)}
.col-1{left:21px;top:550px;width:148px}
.col-1 .rsvp .lead{white-space:nowrap;font-size:11px}
.col-2{left:194px;top:598px;width:148px}
.col-2 .cta{font-size:16px}
.col-3{left:366px;top:592px;width:148px}
</style>
</head>
<body>

<section class="flyer flyer--front">
  <h1 class="council-title">Crossroads Young Leaders Circle<br>of Maple Valley's</h1>
  <div class="partner-box partner-box--left"><span class="partner-name">Bright Harbor<br>Allies</span></div>
  <div class="edition"><div class="edition-year">13th Annual</div><div class="edition-name">Lantern Gathering<br>and Summit</div></div>
  <div class="partner-box partner-box--right"><span class="partner-dot"></span><span class="partner-name">Crossroads Young Leaders Circle of Maple Valley</span></div>
  <p class="tagline">Teens expressing their faith through art, music, and dialogue</p>
  <div class="theme-panel">
    <div class="big">INTERFAITH</div>
    <div class="mid">YOUTH FORUM</div>
    <div class="mid" style="margin-top:12px">THIS YEAR'S<br>THEME IS</div>
    <div class="theme">Religion Cool?</div>
  </div>
  <div class="photo p1" role="img" aria-label="Photo of students mingling at the forum"></div>
  <div class="photo p2" role="img" aria-label="Photo of a framed award on a table"></div>
  <div class="photo p3" role="img" aria-label="Photo of a youth choir singing"></div>
  <div class="photo p4" role="img" aria-label="Photo of a speaker addressing the group"></div>
  <div class="photo p5" role="img" aria-label="Photo of teens performing music with tabla and harmonium"></div>
  <div class="photo p6" role="img" aria-label="Photo of a young drummer"></div>
  <div class="photo p7" role="img" aria-label="Photo of a student playing tabla"></div>
  <div class="photo p8" role="img" aria-label="Photo of a full hall of discussion tables"></div>
  <div class="photo p9" role="img" aria-label="Photo of a table with faith tradition banners and candles"></div>
  <div class="photo p10" role="img" aria-label="Photo of a dancer in traditional dress"></div>
  <div class="photo p11" role="img" aria-label="Photo of a group of students posing"></div>
</section>

<section class="flyer flyer--back">
  <h1 class="council-title">Crossroads Young Leaders Circle<br>of Maple Valley's</h1>
  <div class="partner-box partner-box--left"><span class="partner-name">Bright Harbor<br>Allies</span></div>
  <div class="edition"><div class="edition-year">13th Annual</div><div class="edition-name">Lantern Gathering<br>and Summit</div></div>
  <div class="partner-box partner-box--right"><span class="partner-dot"></span><span class="partner-name">Crossroads Young Leaders Circle of Maple Valley</span></div>
  <p class="tagline">Teens expressing their faith through art, music, and dialogue</p>
  <div class="forum-head forum-head--label">Interfaith Youth Forum</div>
  <div class="forum-head forum-head--intro">This year's theme is</div>
  <div class="forum-head forum-head--theme">Religion Cool?</div>
  <div class="info-band">
    <div class="when"><div>SUNDAY<br>March 19th, 2017</div><div>TIME<br>11:00am-5:00pm</div></div>
    <div class="venue"><strong>Lakeside Fellowship Hall</strong>4150 Orchard Lane, Maple Valley, CA 90210</div>
    <p class="invite">All high school age faith groups are invited to come and join with 150 to 175 other high school students from various faith traditions to participate in the Crossroads Young Leaders Circle of Maple Valley's Annual Interfaith Youth Forum. More than ever, our county and world need young leaders who are willing to learn from each other and build stronger communities!</p>
  </div>
  <div class="detail-col col-1">
    <h3>LANTERN SUMMIT</h3>
    <p>The purpose of this Interfaith Youth Forum is to bring together young people from diverse ethnic, cultural, and religious backgrounds, and to engage them in dialogue. True dialogue is a conversation on a common subject between two or more persons of differing points of view and/or backgrounds. We feel that this commitment to dialogue will affect relationships in a constructive way in our places of worship and in our community.</p>
    <p style="margin-top:6px">The forum itself involves having eight religiously diverse high school-age students, one adult, and youth leader around each table to discuss common questions. Our youth leaders act as facilitators, but it is stressed that it is the students we want to hear from.</p>
    <div class="rsvp" style="margin-top:10px"><span class="lead">RSVP for our LANTERN SUMMIT BY</span><em>FEBRUARY<br>19th, 2017</em></div>
  </div>
  <div class="detail-col col-2">
    <h3>LANTERN GATHERING</h3>
    <p>The forum will be followed by the Lantern Gathering where families of the participants are welcomed to join. The Gathering will include musical performances of all types from diverse religious communities. The differing performing arts include but are not limited to singing, dancing, instrumental music, storytelling, etc. Participate in our</p>
    <div class="cta">LANTERN GATHERING</div>
    <div class="rsvp">(MUSIC, SONG, DANCE)<br>RSVP BY<em>FEBRUARY<br>25th, 2017</em></div>
  </div>
  <div class="detail-col col-3">
    <h3>ART GALLERY</h3>
    <p>This event will include an Art Gallery display of students' work, highlighting their expressions of faith, and artwork promoting learning, understanding, leadership, and service. Art includes any painting, illustration, sculpture, photography or other visual art.</p>
    <div class="cta">ART WORK</div>
    <div class="rsvp">FOR OUR</div>
    <div class="cta">ART GALLERY</div>
    <div class="rsvp">MUST BE SUBMITTED BY<em>MARCH<br>10th, 2017</em></div>
  </div>
</section>

</body>
</html>
```